Home Page Improvement for Web Application

Need drastic home page improvement. Currently it looks very amateur.
Basic navigation text elements position must remain due to CSS (See attached template). However, everything else must be redesigned. Fonts,size, typeface, styles, color, layers, backgrounds, images, buttons, logo typeface, etc. Needs to look fresh, original, sleek, balanced, beautiful and professional.
Target Market(s)
Corporate to small business clients
Professional Instructional Designers
Industry/Entity Type
It Professional
Requirements
Must have
- IMPORTANT! The is a web application and not a website.
Take a look at Plumtide and Post Badger as good designs of web applications.
http://www.pixelharborhub.com/2010/02/showcase-of-great-web-app-interfaces/
Good example of keeping the colors simple:
http://vell.com/
Nice to have
- Some white space.
Min use of new font styles: http://www.brightquillreview.com/2009/08/07/beautiful-new-free-fonts-for-your-designs/
Use of creative navigation styles:
http://www.brightquillreview.com/2010/01/04/showcase-of-modern-navigation-design-trends/
Should not have
- Generic clipart or icons.
Not too dark.
Mismatched fonts.
clashing color schemes.
The same mock style as the attached template.

```html
<!DOCTYPE html>
<html lang="en">
<head>
<meta charset="utf-8">
<title>Coursemeet</title>
<link href="https://fonts.googleapis.com/css2?family=Open+Sans:wght@400;600;700&family=Caveat:wght@600&display=swap" rel="stylesheet">
<style>
:root{
  --blue:#1f6fb8;
  --blue-dark:#165a98;
  --nav-top:#6f8fb8;
  --nav-bot:#4d6d99;
  --cyan:#27a6d6;
  --tab-bar:#8fc9e8;
  --stage:#e9ecef;
  --text:#222;
  --muted:#6b6b6b;
}
*{margin:0;padding:0;box-sizing:border-box}
html,body{width:828px;height:1200px;overflow:hidden;background:#fff}
body{position:relative;font-family:"Open Sans",Arial,sans-serif;color:var(--text)}
.abs{position:absolute}
.logo{left:12px;top:26px;font-size:30px;font-weight:700;color:var(--blue);letter-spacing:-.3px}
.top-btn{top:8px;height:42px;background:linear-gradient(#5f9de0,#3f7cc6);color:#fff;font-size:17px;border-radius:6px;display:flex;align-items:center;justify-content:center}
.main-nav{left:0;top:80px;width:828px;height:36px;background:linear-gradient(var(--nav-top),var(--nav-bot))}
.main-nav span{position:absolute;top:8px;color:#fff;font-size:14px}
.stage{left:0;top:116px;width:828px;height:372px;background:var(--stage)}
.hero{left:95px;top:138px;width:560px;height:332px;background:#fff;border:1px solid #cfd4d9}
.how{left:112px;top:146px;width:150px;height:50px;background:linear-gradient(135deg,#333,#888);border-radius:4px}
.steps{left:205px;top:206px;font-family:"Caveat",cursive;font-size:28px;line-height:44px;color:#222;list-style:none}
.device{left:500px;top:176px;width:140px;height:132px;background:linear-gradient(#cfd6dd,#8fa0b0);border-radius:6px}
.bubble{top:386px;height:56px;background:linear-gradient(#6fa4dd,#3d78c0);color:#fff;border-radius:10px;text-align:center;font-size:12px;padding-top:7px}
.bubble b{display:block;font-size:15px;margin-top:3px}
.side-tab{left:650px;top:138px;width:75px;height:332px;background:linear-gradient(90deg,#4c8fd6,#2d6fbd)}
.side-tab span{position:absolute;color:#fff;writing-mode:vertical-rl;font-size:26px;left:20px}
.search-band{left:0;top:488px;width:828px;height:57px;background:var(--blue)}
.search-label{left:155px;top:503px;color:#fff;font-size:19px}
.search-input{left:383px;top:503px;width:207px;height:28px;background:#fff;border:1px solid #c8d6e6}
.post-btn{left:615px;top:500px;width:90px;height:34px;background:#5a92d3;color:#fff;border-radius:6px;font-size:18px;display:flex;align-items:center;justify-content:center}
.tab-bar{left:0;top:545px;width:828px;height:43px;background:var(--tab-bar)}
.tab{position:absolute;top:553px;font-size:13px;color:#fff}
.tab.active{left:35px;top:549px;width:148px;height:39px;background:#fff;color:var(--blue);padding:6px 0 0 16px}
.shot{top:600px;width:252px;height:196px;border:1px solid #bbb}
.meta{font-size:12px;line-height:25px;top:798px;width:260px}
.meta b{font-weight:700}
.foot-head{top:915px;height:30px;background:var(--cyan);color:#fff;font-size:17px;font-weight:600;text-align:center;line-height:30px}
.links{top:966px;font-size:13px;line-height:26px;color:var(--muted)}
.social{top:970px;width:30px;height:30px;border-radius:4px}
.rule{left:10px;top:1132px;width:808px;height:1px;background:#ccc}
.copy{left:18px;top:1150px;font-size:12px;color:var(--muted)}
.copy i{display:inline-block;width:18px;height:18px;border:1px solid #999;border-radius:50%;font-style:normal;text-align:center;line-height:16px;font-size:11px;margin-right:6px}
.copy a{color:var(--cyan)}
</style>
</head>
<body>
<div class="abs logo">Coursemeet</div>
<div class="abs top-btn" style="left:518px;width:146px">Post A Project</div>
<div class="abs top-btn" style="left:700px;width:118px">Projects</div>

<nav class="abs main-nav">
  <span style="left:35px">Home</span>
  <span style="left:150px">Projects</span>
  <span style="left:293px">Designers</span>
  <span style="left:445px">Templates</span>
</nav>

<div class="abs stage"></div>
<section class="abs hero"></section>
<div class="abs how" role="img" aria-label="Hand-lettered 'How It Works' banner"></div>
<ol class="abs steps">
  <li>1. Post Your project</li>
  <li>2. Determine Your budget</li>
  <li>3. Select the Best Design</li>
</ol>
<div class="abs device" role="img" aria-label="Laptop with mouse illustration"></div>
<div class="abs bubble" style="left:105px;width:165px">Describe Your Project<b>Authorly WBT</b></div>
<div class="abs bubble" style="left:285px;width:165px">Budget Your Project<b>Fixedbid $1000</b></div>
<div class="abs bubble" style="left:468px;width:165px">Award Your Project<b>Best Designer</b></div>
<div class="abs side-tab">
  <span style="top:20px">Projects</span>
  <span style="top:170px;font-size:20px;left:14px">Instructional Designers</span>
</div>

<div class="abs search-band"></div>
<div class="abs search-label">ProjectName</div>
<div class="abs search-input"></div>
<div class="abs post-btn">+ Post</div>

<div class="abs tab-bar"></div>
<div class="abs tab active">Open projects (20)</div>
<div class="tab" style="left:202px">Designers Available(100)</div>
<div class="tab" style="left:370px">Projects in progress (52)</div>
<div class="tab" style="left:537px">Projects Completed (564)</div>
<div class="tab" style="left:710px">Templates</div>

<div class="abs shot" style="left:10px;background:linear-gradient(#1b4fa8,#0a1a4a)" role="img" aria-label="Business silhouettes against blue light"></div>
<div class="abs shot" style="left:290px;background:linear-gradient(#7fc7ef,#2a6fb0)" role="img" aria-label="Colourful course interface screenshot"></div>
<div class="abs shot" style="left:573px;background:linear-gradient(#2a5fa8,#0e2a60)" role="img" aria-label="Blue course template screenshot"></div>

<div class="abs meta" style="left:10px"><b>Project name</b>: Sales Training WBT<br><b>Authoring Tool:</b> Slidecraft 4.0<br><b>Skill Requirements</b>: Retail/Sales Knowledge</div>
<div class="abs meta" style="left:290px"><b>Project name</b>: Sales Training WBT<br><b>Authoring Tool:</b> Slidecraft 4.0<br><b>Skill Requirements</b>: Retail/Sales Knowledge</div>
<div class="abs meta" style="left:573px"><b>Project name</b>: Sales Training WBT<br><b>Authoring Tool:</b> Slidecraft 4.0<br><b>Skill Requirements</b>: Retail/Sales Knowledge</div>

<div class="abs foot-head" style="left:38px;width:152px">How to</div>
<div class="abs foot-head" style="left:233px;width:167px">Customer Service</div>
<div class="abs foot-head" style="left:433px;width:157px">Knowledge Base</div>
<div class="abs foot-head" style="left:633px;width:157px">Stay In Touch</div>

<div class="abs links" style="left:50px">Managing projects<br>Awarding your project<br>Final Changes<br>Entering A Project<br>What if you Win!</div>
<div class="abs links" style="left:232px">Support<br>Submit a Request<br>Check your existing requests</div>
<div class="abs links" style="left:458px">FAQ General<br>FAQ Project<br>FAQ Designer<br>Announcements<br>Feature Requests<br>Tips &amp; Tricks</div>

<div class="abs social" style="left:645px;background:#8cc63f"></div>
<div class="abs social" style="left:683px;background:#3b5998"></div>
<div class="abs social" style="left:721px;background:#5bc0eb"></div>
<div class="abs social" style="left:759px;background:#f08a24"></div>

<div class="abs rule"></div>
<div class="abs copy"><i>C</i>2011, Coursemeet, All rights reserved. Use of this service and this website constitutes acceptance of our <a>terms</a></div>
</body>
</html>
```